Korbin Ventilation's. "We're Dalton beyond the pack"!

Good day< Does your company do face mask? that is question 1. and lets finish the stationary design and I will pay for that now? 2 If your company has BLACK HATS now I would want to do some of those? 3 I notice do you do BANNER'S and or something I can put on van's magnet type or on a building! )k that's enough but for now lets start with the stationary stuff? let me know you should have my information, and the design look's GREAT!!! Thank you..

```html
<!DOCTYPE html>
<html lang="en">
<head>
<meta charset="utf-8">
<title>Korbin Ventilation's — Letterhead</title>
<link rel="stylesheet" href="https://fonts.googleapis.com/css2?family=Open+Sans:wght@400;600&family=Arimo&family=Lato:wght@400&display=swap">
<style>
  :root {
    --ink: #000000;
    --lime: #bedc5a;
    --paper: #ffffff;
    --text: #4a4a4a;
    --dark-text: #222222;
    --backdrop: #e9e9e9;
  }
  * { margin: 0; padding: 0; box-sizing: border-box; }
  html, body {
    width: 1040px; height: 1200px; overflow: hidden;
    background: var(--backdrop);
  }
  .letterhead {
    position: absolute; left: 54px; top: 0;
    width: 790px; height: 1017px;
    background: var(--paper);
    transform: scale(1.18);
    transform-origin: top left;
    font-family: "Open Sans", sans-serif;
    color: var(--text);
  }
  .frame { position: absolute; inset: 0; width: 790px; height: 1017px; }
  .brand {
    position: absolute; left: 110px; top: 26px; width: 180px;
    text-align: center; color: var(--ink);
    font-family: "Open Sans", sans-serif; font-weight: 600;
  }
  .brand-dot {
    width: 46px; height: 46px; border-radius: 50%;
    background: var(--ink); margin: 0 auto 8px;
  }
  .brand-name { font-size: 19px; line-height: 21px; }
  .brand-tagline { font-size: 11px; margin-top: 3px; }
  .contact {
    position: absolute; left: 545px; top: 36px;
    font-family: "Arimo", sans-serif; font-size: 14px; color: var(--ink);
    list-style: none;
  }
  .contact li { display: flex; align-items: center; height: 17px; }
  .contact svg { width: 12px; height: 12px; margin-right: 7px; }
  .letter { position: absolute; left: 74px; top: 184px; width: 638px; font-size: 12.5px; }
  .issue-date { margin-bottom: 14px; }
  .recipient p { line-height: 15px; }
  .salutation { margin-top: 42px; margin-bottom: 25px; }
  .body-copy p { line-height: 23px; text-align: justify; margin-bottom: 22px; }
  .closing { margin-top: 35px; }
  .signatory { margin-top: 44px; }
  .signatory-name { font-size: 15.5px; font-weight: 600; color: var(--dark-text); }
  .signatory-role { margin-top: 4px; }
  .footer-address {
    position: absolute; left: 0; right: 0; top: 983px;
    text-align: center; color: var(--paper);
    font-family: "Lato", sans-serif; font-size: 15px;
  }
</style>
</head>
<body>
<div class="letterhead">
  <svg class="frame" viewBox="0 0 790 1017" aria-hidden="true">
    <path d="M0 0 H700 L220 6 C80 18 18 100 0 205 Z" fill="var(--ink)"/>
    <path d="M0 212 C20 104 82 24 222 12 L700 0" fill="none" stroke="var(--lime)" stroke-width="4"/>
    <path d="M790 765 C784 905 724 972 560 976 L0 979 V1017 H790 Z" fill="var(--ink)"/>
    <path d="M788 752 C782 895 722 964 558 968 L0 972" fill="none" stroke="var(--lime)" stroke-width="4"/>
  </svg>

  <div class="brand">
    <div class="brand-dot"></div>
    <div class="brand-name">Korbin<br>Ventilation's</div>
    <div class="brand-tagline">"We're Dalton beyond the pack"</div>
  </div>

  <ul class="contact">
    <li><svg viewBox="0 0 12 12"><path d="M2.5 1 L4.5 1 L5.2 3.6 L4 4.6 C4.6 6 6 7.4 7.4 8 L8.4 6.8 L11 7.5 L11 9.5 C11 10.3 10.3 11 9.5 11 C5 11 1 7 1 2.5 C1 1.7 1.7 1 2.5 1 Z" fill="var(--lime)"/></svg>044-123 456 789</li>
    <li><svg viewBox="0 0 12 12"><rect x="0.5" y="2.5" width="11" height="7.5" fill="var(--lime)"/><path d="M0.5 2.5 L6 7 L11.5 2.5" fill="none" stroke="#fff" stroke-width="1"/></svg>info@webname.com</li>
    <li><svg viewBox="0 0 12 12"><circle cx="6" cy="6" r="5" fill="none" stroke="var(--lime)" stroke-width="1.4"/><ellipse cx="6" cy="6" rx="2.2" ry="5" fill="none" stroke="var(--lime)" stroke-width="1"/><path d="M1 6 H11" stroke="var(--lime)" stroke-width="1"/></svg>www.websitename.com</li>
  </ul>

  <main class="letter">
    <p class="issue-date">Issuing Date: May 5, 2018</p>
    <div class="recipient">
      <p>Name Of Employee Mr. XYZABC</p>
      <p>Address of Employee</p>
      <p>Address Line 2 etc..</p>
    </div>
    <p class="salutation">Dear Mr.XYZABC</p>
    <div class="body-copy">
      <p>Lorem Ipsum has been the industry's standard dummy text ever since the 1500s, when an unknown printer took a galley of type and scrambled it to make a type specimen book. It has survived not only five centuries, but also the leap into electronic typesetting, remaining essentially unchanged. It was popularised in the 1960s with the release of Typeline sheets containing Lorem Ipsum passages, and more recently with desktop publishing software like Folio Layout including versions of Lorem Ipsum.</p>
      <p>Lorem Ipsum is simply dummy text of the printing and typesetting industry. Lorem Ipsum has been the industry's standard dummy text ever since the 1500s, when an unknown printer took a galley of type and scrambled it to make a type specimen book.</p>
      <p>It has survived not only five centuries, but also the leap into electronic typesetting, remaining essentially unchanged. It was popularised in the 1960s with the release of Typeline sheets containing Lorem IpsumIpsum passages.</p>
    </div>
    <p class="closing">Yours Sincerely</p>
    <div class="signatory">
      <p class="signatory-name">Marlow Fenwick</p>
      <p class="signatory-role">Managing Director</p>
    </div>
  </main>

  <p class="footer-address">421, Address line here,&nbsp; dummy code 45452 Country Name</p>
</div>
</body>
</html>
```